K&T Fixit and Rebuild general contracting business card design

I already have a logo that I want to use and I need a card that uses that logo and color scheme on the front with the address phone numbers and email and on the back a place for technicians to write in their name and phone number when they hand it out. It will need the License number of License #KTFXTRB318QN.
It should say General Contractor under the company name. The address is
4417 NE 3rd Ave, Ste D246
Vancouver, WA 98612
www.kandtfixitandrebuild.example
office@kandtfixitandrebuild.example
360-555-0182 is the telephone number
360-555-0149 is the fax number

Target Market(s)

Homeowners needing remodel work or repairs in their home.

Industry/Entity Type

Construction

Contact Information for Business Card

Business name, address, phone number, license number, fax number, email, and website on the front and a place to fill in technician's name and number

Font styles to use
Serif

Requirements
Must have
• Business name, address, phone number, license number, fax number, email, and website on the front and a place to fill in technician's name and number
Nice to have
• I uploaded an example of a front that is good.
Should not have
• Froo froo or extra embellishments.

```html
<!DOCTYPE html>
<html lang="en">
<head>
<meta charset="utf-8">
<title>K&amp;T Fixit and Rebuild – Business Card</title>
<link rel="stylesheet" href="https://fonts.googleapis.com/css2?family=Michroma&family=Arimo:wght@400&display=swap">
<style>
  :root {
    --maroon: #600e23;
    --grey-text: #676767;
    --paper: #ffffff;
    --backdrop: #d3d3d3;
  }
  * { box-sizing: border-box; margin: 0; padding: 0; }
  html, body {
    width: 1200px; height: 1200px; overflow: hidden;
    background: var(--backdrop);
  }
  .stage { position: relative; width: 1200px; height: 1200px; }

  .card {
    position: absolute;
    left: 239px; width: 722px; height: 412px;
  }
  .card--front {
    top: 146px;
    background: var(--paper);
    border: 15px solid var(--maroon);
  }
  .card--back {
    top: 642px;
    background: var(--maroon);
  }

  .brand {
    position: absolute;
    font-family: "Michroma", sans-serif;
    text-transform: uppercase;
    line-height: 1.15;
    text-align: center;
  }
  .brand__mark { display: block; font-size: 60px; letter-spacing: 2px; }
  .brand__name { display: block; font-size: 15px; letter-spacing: 0.5px; margin-top: 8px; }
  .brand__role {
    display: block; font-family: "Arimo", sans-serif; text-transform: none;
    font-size: 15px; margin-top: 10px; color: var(--grey-text);
  }
  .brand__license {
    display: block; font-family: "Arimo", sans-serif; text-transform: none;
    font-size: 13px; margin-top: 4px; color: var(--grey-text);
  }

  .card--front .brand { left: 28px; top: 96px; width: 270px; color: var(--maroon); }

  .card--back .brand { left: 0; right: 0; top: 62px; color: var(--paper); }
  .card--back .brand__mark { font-size: 84px; }
  .card--back .brand__name { font-size: 20px; margin-top: 12px; }

  .divider {
    position: absolute; left: 322px; top: 98px;
    width: 1.5px; height: 192px; background: var(--maroon);
  }

  .contact {
    position: absolute; left: 347px; top: 96px;
    font-family: "Arimo", sans-serif; color: var(--grey-text);
  }
  .contact__name {
    font-family: "Michroma", sans-serif; color: var(--maroon);
    font-size: 20px; letter-spacing: 1px; text-transform: uppercase;
    line-height: 1.1; white-space: nowrap;
  }
  .contact__title { font-size: 16px; margin-top: 3px; }
  .contact__address { font-size: 16px; line-height: 22px; margin-top: 9px; }
  .contact__list { list-style: none; margin-top: 6px; font-size: 16px; }
  .contact__list li { display: flex; align-items: center; height: 22px; white-space: nowrap; }
  .contact__icon { width: 11px; height: 11px; margin-right: 6px; flex: none; }

  .tech-fields {
    position: absolute; left: 120px; right: 120px; top: 278px;
    font-family: "Arimo", sans-serif; color: var(--paper); font-size: 15px;
  }
  .tech-field { display: flex; align-items: flex-end; height: 36px; }
  .tech-field__label { width: 100px; flex: none; }
  .tech-field__line { flex: 1; border-bottom: 1.5px solid var(--paper); height: 1px; margin-bottom: 3px; }
</style>
</head>
<body>
<div class="stage">

  <section class="card card--front" aria-label="Business card front">
    <div class="brand">
      <span class="brand__mark">K&amp;T</span>
      <span class="brand__name">Fixit and Rebuild</span>
      <span class="brand__role">General Contractor</span>
      <span class="brand__license">License #KTFXTRB318QN</span>
    </div>

    <div class="divider"></div>

    <div class="contact">
      <h1 class="contact__name">Daniel Hargrove</h1>
      <p class="contact__title">Director</p>
      <p class="contact__address">4417 NE 3rd Ave, Ste D246<br>Vancouver, WA 98612</p>
      <ul class="contact__list">
        <li>
          <svg class="contact__icon" viewBox="0 0 12 12" aria-hidden="true"><path fill="#600e23" d="M3 1l2 2.5-1 1.2c.6 1.4 1.7 2.5 3.1 3.1l1.2-1L11 8.8 9.6 11C5 10.6 1.4 7 1 2.4z"/></svg>
          360-555-0182
        </li>
        <li>
          <svg class="contact__icon" viewBox="0 0 12 12" aria-hidden="true"><rect x="3" y="1" width="6" height="3" fill="#600e23"/><rect x="1" y="4" width="10" height="5" rx="1" fill="#600e23"/><rect x="3" y="8" width="6" height="3" fill="#600e23"/></svg>
          360-555-0149
        </li>
        <li>
          <svg class="contact__icon" viewBox="0 0 12 12" aria-hidden="true"><rect x="1" y="2.5" width="10" height="7" fill="none" stroke="#600e23" stroke-width="1.2"/><path d="M1 2.5l5 4 5-4" fill="none" stroke="#600e23" stroke-width="1.2"/></svg>
          office@kandtfixitandrebuild.example
        </li>
        <li>
          <svg class="contact__icon" viewBox="0 0 12 12" aria-hidden="true"><g fill="none" stroke="#600e23" stroke-width="0.9"><circle cx="6" cy="6" r="5"/><ellipse cx="6" cy="6" rx="2.2" ry="5"/><path d="M1 6h10M2 3.5h8M2 8.5h8"/></g></svg>
          www.kandtfixitandrebuild.example
        </li>
      </ul>
    </div>
  </section>

  <section class="card card--back" aria-label="Business card back">
    <div class="brand">
      <span class="brand__mark">K&amp;T</span>
      <span class="brand__name">Fixit and Rebuild</span>
    </div>
    <div class="tech-fields">
      <div class="tech-field"><span class="tech-field__label">Technician</span><span class="tech-field__line"></span></div>
      <div class="tech-field"><span class="tech-field__label">Phone</span><span class="tech-field__line"></span></div>
    </div>
  </section>

</div>
</body>
</html>
```